Need design for Vinyl window signs

I need Vinyl window sign to cover my front retail pharmacy window. Not the whole window area i want there to be open areas so people can still see inside.
Attached is the pic of front door and also the logo which contains the colors we want to use. The width of the door is about 14ft wide and 7ft high and its 3 sections. The middle section the door is 36 inch.

And the vinyl graphic should include the following info:
Ellerby Grove pharmacy
Caring for you, Caring for the community

Wellness starts here!
Locally owned independent pharmacy
No wait
Same Copay as chains
Free local delivery

We do prescriptions, private consultations, compounding, immunizations, travel health and other clinical services

We also provide free blood pressure, blood glucose and blood oxygen testing everyday.
No appointments necessary.

Write Pharmacy in different languages: Spanish, Farsi, Hebrew, Russian

Phone: 555-286-4907

Hours:
M- F 9-6
Sat and sun and major Holliday: closed

Target Market(s)

Patients: People seeking medication or health advice. Caregivers: Those caring for others who need prescriptions. Health-Conscious Individuals: People interested in preventive health measures. Chronic Condition Sufferers: Individuals managing ongoing health issues. Healthcare Professionals: Doctors and nurses who may refer patients to pharmacists.

Industry/Entity Type

Retail pharmacy

Font styles to use
Sans Serif

Colors
0054AA
0677BA
7BADD7
CADEEF
E8F1F8
00AB8E
00BBA5
67D7C9
C6EFE9
E9F9F6

Requirements
Must have
• At least 3 sections for each window left side and right side and middle area, must have Green and blue color to match my logo see attached.
Nice to have
• Like to see a pics or two of people maybe seniors and younger adults enjoying their time

```html
<!DOCTYPE html>
<html lang="en">
<head>
<meta charset="utf-8">
<title>Ellerby Grove Pharmacy – Window Signs</title>
<link href="https://fonts.googleapis.com/css2?family=Montserrat:wght@600;700;800;900&family=Roboto:wght@500;700&family=Kalam:wght@400&display=swap" rel="stylesheet">
<style>
  :root{
    --blue:#1f7bc4;
    --blue-light:#3a8fd2;
    --green:#62a83f;
    --green-dark:#559a35;
    --white:#ffffff;
    --page:#eef1f4;
  }
  *{box-sizing:border-box;margin:0;padding:0}
  html,body{width:1200px;height:849px;overflow:hidden;background:var(--page)}
  body{position:relative;font-family:"Montserrat",sans-serif;color:var(--white)}
  .window-set{position:absolute;left:26px;top:138px;width:1148px;height:573px}
  .panel{position:absolute;top:0;height:573px;overflow:hidden;background:var(--green)}
  .panel-left{left:0;width:446px}
  .panel-middle{left:473px;width:207px}
  .panel-right{left:712px;width:436px}
  .panel-shape{position:absolute;inset:0}
  .abs{position:absolute}
  .center{text-align:center;transform:translateX(-50%)}

  .hero-photo{position:absolute;left:-42px;top:8px;width:304px;height:304px;border-radius:50%;
    border:8px solid var(--green);
    background:radial-gradient(circle at 45% 40%,#e6d3c4 0%,#b89a88 35%,#3e4a66 70%,#2a3350 100%)}
  .headline{left:209px;top:144px;font-weight:900;font-size:33px;line-height:37px;letter-spacing:.3px;
    text-shadow:2px 2px 3px rgba(0,0,0,.45)}
  .services-title{left:223px;top:325px;font-weight:800;font-size:16px;white-space:nowrap}
  .services-text{left:223px;top:350px;width:320px;font-weight:700;font-size:11.5px;line-height:15px}

  .outline-box{position:absolute;border:2px solid var(--white);border-radius:12px}
  .pill{position:absolute;background:var(--white);border-radius:5px;font-weight:800;white-space:nowrap;
    transform:translate(-50%,-50%);box-shadow:1px 2px 3px rgba(0,0,0,.3);text-align:center}
  .free-box{left:42px;top:441px;width:362px;height:111px}
  .free-label{left:223px;top:441px;width:168px;font-size:16px;line-height:26px;color:var(--green)}
  .test-item{position:absolute;top:468px;width:100px;transform:translateX(-50%);text-align:center}
  .test-item svg{display:block;margin:0 auto;width:40px;height:40px}
  .test-label{font-weight:800;font-size:11px;line-height:12px;margin-top:14px}

  .brand-mark{left:103px;top:31px;width:110px;height:110px;border-radius:50%;background:var(--white);
    transform:translateX(-50%);display:flex;align-items:center;justify-content:center;
    color:var(--blue);font-weight:800;font-size:15px;line-height:17px;text-align:center}
  .brand-mark::before{content:"";position:absolute;inset:6px;border:5px solid var(--blue);border-radius:50%}
  .lang{left:103px;font-family:"Roboto",sans-serif;font-weight:500;font-size:25px;white-space:nowrap;transform:translate(-50%,-50%)}
  .pharmacy-name{left:103px;top:370px;font-weight:900;font-size:26px;line-height:30px;white-space:nowrap}
  .tagline{left:103px;top:474px;font-family:"Kalam",cursive;font-size:16px;line-height:22px;white-space:nowrap}

  .promise-box{left:62px;top:109px;width:311px;height:166px}
  .promise-label{left:217px;top:109px;width:222px;font-size:20px;line-height:28px;color:var(--blue)}
  .promise-list{left:217px;top:140px;list-style:none;font-weight:800;font-size:15.5px;line-height:32px;white-space:nowrap}
  .hours{left:217px;top:357px;font-family:"Roboto",sans-serif;font-weight:700;font-size:33px;white-space:nowrap;
    text-shadow:2px 2px 3px rgba(0,0,0,.4)}
  .closed-note{left:217px;top:425px;font-family:"Roboto",sans-serif;font-weight:500;font-size:14px;line-height:20px;white-space:nowrap}
  .appt-pill{left:218px;top:497px;width:272px;font-size:13.5px;line-height:22px;color:var(--green)}
  .phone{left:218px;top:515px;font-family:"Roboto",sans-serif;font-weight:700;font-size:41px;white-space:nowrap}
</style>
</head>
<body>
<main class="window-set">

  <section class="panel panel-left">
    <svg class="panel-shape" viewBox="0 0 446 573" aria-hidden="true">
      <defs>
        <linearGradient id="blueFadeL" x1="0" y1="0" x2="1" y2="0">
          <stop offset="0" stop-color="#1f7bc4"/><stop offset="1" stop-color="#3487cb"/>
        </linearGradient>
      </defs>
      <path d="M0 0H446V339H425L405 395Q401 406 388 408H85Q72 406 66 395L45 339H0Z" fill="url(#blueFadeL)" style="filter:drop-shadow(2px 3px 2px rgba(0,0,0,.35))"/>
    </svg>
    <div class="hero-photo" role="img" aria-label="Photo of a smiling senior couple embracing"></div>
    <h1 class="headline abs">WELLNESS<br>STARTS<br>HERE!</h1>
    <h2 class="services-title abs center">WHAT WE DO?</h2>
    <p class="services-text abs center">Prescriptions, Private Consultations, Compounding, Immunizations, Travel Health And Other Clinical Services.</p>

    <div class="outline-box free-box"></div>
    <div class="pill free-label">FREE EVERYDAY</div>

    <div class="test-item" style="left:102px">
      <svg viewBox="0 0 40 40" fill="none" stroke="#fff" stroke-width="3" stroke-linecap="round">
        <circle cx="29" cy="11" r="7"/><path d="M29 11l3-3"/><path d="M29 18v6q0 8-9 8h-4"/><ellipse cx="10" cy="30" rx="6" ry="8" fill="#fff"/>
      </svg>
      <div class="test-label">BLOOD<br>PRESSURE</div>
    </div>
    <div class="test-item" style="left:223px">
      <svg viewBox="0 0 40 40" fill="none" stroke="#fff" stroke-width="3" stroke-linecap="round">
        <rect x="2" y="6" width="12" height="8" rx="2"/><path d="M14 10h6"/><path d="M24 38V16M29 38V10M34 38V14M24 38h12V22"/>
      </svg>
      <div class="test-label">BLOOD<br>GLUCOSE</div>
    </div>
    <div class="test-item" style="left:344px">
      <svg viewBox="0 0 40 40" fill="none" stroke="#fff" stroke-width="3" stroke-linecap="round">
        <rect x="14" y="2" width="10" height="12" rx="2"/><path d="M19 14v14M19 38h14V24l-8-2"/><path d="M19 28l-6-4" />
      </svg>
      <div class="test-label">BLOOD<br>OXYGEN</div>
    </div>
  </section>

  <section class="panel panel-middle">
    <svg class="panel-shape" viewBox="0 0 207 573" aria-hidden="true">
      <rect width="207" height="339" fill="#1f7bc4"/>
    </svg>
    <div class="brand-mark abs">Ellerby<br>Grove</div>
    <p class="lang abs" style="top:188px">Farmacia</p>
    <p class="lang abs" style="top:222px" lang="fa" dir="rtl">داروخانه</p>
    <p class="lang abs" style="top:261px" lang="he" dir="rtl">בֵּית מִרקַחַת</p>
    <p class="lang abs" style="top:296px" lang="ru">Аптека</p>
    <h2 class="pharmacy-name abs center">ELLERBY<br>GROVE<br>PHARMACY</h2>
    <p class="tagline abs center">Caring for you,<br>Caring for the community</p>
  </section>

  <section class="panel panel-right">
    <svg class="panel-shape" viewBox="0 0 436 573" aria-hidden="true">
      <path d="M0 0H436V339H408L388 395Q384 406 371 408H88Q75 406 69 395L48 339H0Z" fill="#1f7bc4" style="filter:drop-shadow(2px 3px 2px rgba(0,0,0,.35))"/>
    </svg>
    <div class="outline-box promise-box"></div>
    <div class="pill promise-label">LOCALLY OWNED</div>
    <ul class="promise-list abs center">
      <li>INDEPENDENT PHARMACY</li>
      <li>NO WAIT</li>
      <li>SAME COPAY AS CHAINS</li>
      <li>FREE LOCAL DELIVERY</li>
    </ul>
    <p class="hours abs center">Hours: M-F 9-6</p>
    <p class="closed-note abs center">Saturday and Sunday and<br>Major Holliday: closed</p>
    <div class="pill appt-pill">NO APPOINTMENTS NECESSARY</div>
    <p class="phone abs center">555-286-4907</p>
  </section>

</main>
</body>
</html>
```